ZESTORAMA Business Card Design

ZESTORAMA
Zestorama is a food van, serving high vibe delicious food to go. This business is dedicated to healthy delicious feel good food, beauty in service and a sustainable planet.

The van will operate in the south west of western Australia at music festivals events markets wherever people need great food to go!

I like the idea of vibrant green mixed with a yellow?? background with some rays like the sun through the background.
The font needs to say vibrant energetic
TO ME -vibrant energetic font has to appear to be on the move - perhaps with shading??

I like fusha if that works for font? but the colour has to say food too.

I would like a symbol on the card a simple V turned into a womans raised arms. This should be vibrant too.
Thank you
Blessings
Marisol

Target Market(s)

target lovers of healthy high vibe food. music festival goers. age 18- 50 feel. audiance conscious eaters of feel great food

Industry/Entity Type

Events

Contact Information for Business Card

ZESTORAMA
High Vibe Food
Van
Marisol -owner/opperator
0417385960
Face book symbol - ZESTORAMA

on the I would like a logo of a simple V turned into a womans arms up toward the sky flip side

My number and name again
Zestorama- feel great mobile food
Festivals, events, markets & where high vibe food 2 go is appreciated

Requirements
Nice to have
• Moving energetic font
colour that says high vibe and healthy food

a logo that is a simple V turned into a woman's raised arms in gratitude

```html
<!DOCTYPE html>
<html lang="en">
<head>
<meta charset="utf-8">
<title>Zestorama Business Card</title>
<link rel="stylesheet" href="https://fonts.googleapis.com/css2?family=Didact+Gothic&display=swap">
<style>
  :root {
    --green: #3e9b2b;
    --green-light: #8fcf45;
    --green-deep: #2f8a22;
    --yellow: #f5c518;
    --orange: #f0a41c;
    --white: #ffffff;
    --backdrop: #eeeeea;
    --ray-pale: #f1f7e4;
  }
  * { box-sizing: border-box; margin: 0; padding: 0; }
  html, body { width: 1200px; height: 784px; overflow: hidden; }
  body {
    background: var(--backdrop);
    font-family: "Didact Gothic", "Century Gothic", sans-serif;
    display: flex;
    align-items: center;
    justify-content: center;
    gap: 40px;
  }
  .card {
    position: relative;
    width: 540px;
    height: 310px;
    overflow: hidden;
    box-shadow: 0 6px 18px rgba(0,0,0,0.18);
  }

  /* Front side */
  .card-front {
    background: radial-gradient(ellipse 70% 85% at 50% 30%, var(--ray-pale) 0%, var(--white) 70%);
  }
  .front-figure {
    position: absolute;
    left: 200px; top: 22px;
    width: 140px; height: 130px;
    border-radius: 50% 50% 45% 45%;
    background: radial-gradient(ellipse at 50% 45%, rgba(95,170,50,0.55), rgba(245,197,24,0.25) 70%, transparent 75%);
  }
  .brand-name {
    position: absolute;
    left: 0; right: 0; top: 140px;
    text-align: center;
    font-size: 42px;
    letter-spacing: 1px;
    color: var(--green);
  }
  .brand-tagline {
    position: absolute;
    left: 0; right: 0; top: 192px;
    text-align: center;
    font-size: 18px;
    letter-spacing: 1px;
    color: var(--orange);
    z-index: 2;
  }
  .contact-band {
    position: absolute;
    left: 0; right: 0; top: 186px; height: 106px;
    background: linear-gradient(180deg, var(--green-light) 0%, var(--green) 100%);
    border-top: 3px solid var(--yellow);
    border-bottom: 3px solid var(--yellow);
  }
  .contact-band .contact-block { top: 28px; }
  .social-square {
    position: absolute;
    right: 20px; top: 160px;
    width: 16px; height: 16px;
    background: var(--green-deep);
  }
  .contact-block {
    position: absolute;
    left: 0; right: 0;
    text-align: center;
    color: var(--white);
    line-height: 1.1;
  }
  .contact-name { font-size: 21px; letter-spacing: 1px; }
  .contact-role { font-size: 13px; letter-spacing: 1px; }
  .contact-phone { font-size: 25px; letter-spacing: 2px; }

  /* Back side */
  .card-back {
    background: radial-gradient(ellipse 75% 90% at 50% 25%, var(--green-light) 0%, var(--green) 75%);
  }
  .back-figure {
    position: absolute;
    left: 180px; top: 10px;
    width: 180px; height: 180px;
    border-radius: 50% 50% 45% 45%;
    background: radial-gradient(ellipse at 50% 45%, rgba(47,138,34,0.8), rgba(245,197,24,0.35) 68%, transparent 74%);
  }
  .card-back .contact-block { top: 60px; }
  .back-slogan {
    position: absolute;
    left: 0; right: 0; bottom: 30px;
    text-align: center;
    color: var(--white);
    font-size: 14px;
    letter-spacing: 2px;
    line-height: 1.25;
  }
</style>
</head>
<body>
  <section class="card card-front">
    <div class="front-figure" role="img" aria-label="Illustration of a woman with raised arms inside a yellow ring, over sun rays"></div>
    <div class="brand-name">ZESTORAMA</div>
    <div class="social-square"></div>
    <div class="contact-band">
      <div class="contact-block">
        <div class="contact-name">Marisol</div>
        <div class="contact-role">owner/opperator</div>
        <div class="contact-phone">0417385960</div>
      </div>
    </div>
    <div class="brand-tagline">High Vibe Food Van</div>
  </section>

  <section class="card card-back">
    <div class="back-figure" role="img" aria-label="Illustration of a woman with raised arms inside a yellow ring, over sun rays"></div>
    <div class="contact-block">
      <div class="contact-name">Marisol</div>
      <div class="contact-role">owner/opperator</div>
      <div class="contact-phone">0417385960</div>
    </div>
    <p class="back-slogan">feel great mobile food Festivals, events,<br>markets &amp; where high vibe food 2 go is appreciated</p>
  </section>
</body>
</html>
```